Fresh, modern brand required for new start-up!

TallCedarRun is a new venture offering an end-to-end communications and media relations service including strategy development, execution and evaluation; copy writing and editing; social and e- media management; leadership coaching, media training and more.

I require a fresh and lively corporate identity to mirror the ethos of the business.

I need a logo, business card (double-sided preferably), letterhead (for invoicing and client communications) and compliment slip. As a start-up, budget will be an ongoing consideration for me so, ideally, I would prefer a two-colour logo - although if you wow me with something more than that, I may have to throw caution to the wind!

The ethos behind my name is twofold; one, I have moved from being something of a "big fish in a small pond" (a director in a single company) to a small fish in the big pond of small businesses. Two, I may be a "small fish", but that doesn't mean I don't "fish big".

I am looking for a clean, simple design that will look good on a variety of mediums, big or small. The design should be young and fresh and make an immediate impact. I want the design to reflect the fact that I specialise in tailored, simple and effective communications.

Target Market(s)

My clients range from global financial services, resources and technology companies to not-for-profit organisations and other small businesses. Moreover, my current client base stretches from Asia Pacific (incl. Australia), to Europe (incl. UK) and the US. All my clients speak English (even if as a second language) and are relatively senior communications professionals within their organisations.

Industry/Entity Type

Communications

Requirements
Nice to have
• The design/logo could include symbols and/or characters that double as imagery. For example: an upside down question mark (?) might look like a fishing line/hook and a flattened @ sign, might look like a pond...
Should not have
• The design should not use old-style serif fonts, but nor should it be "cartoony" in any way. No navy blue, grey or sombre corporate colours.

```html
<!DOCTYPE html>
<html lang="en">
<head>
<meta charset="utf-8">
<title>TallCedarRun – Stationery Set</title>
<link href="https://fonts.googleapis.com/css2?family=Mulish:ital,wght@0,700;0,800;1,400&family=Questrial&display=swap" rel="stylesheet">
<style>
  :root{
    --orange:#ff8000;
    --blue:#4012f2;
    --white:#ffffff;
    --paper:#ffffff;
    --shadow:rgba(0,0,0,.35);
  }
  *{box-sizing:border-box;margin:0;padding:0}
  html,body{width:900px;height:1200px;overflow:hidden;background:var(--paper)}
  body{position:relative;font-family:"Mulish",sans-serif;color:var(--white)}

  .card{position:absolute;top:56px;width:302px;height:465px;box-shadow:6px 8px 10px var(--shadow)}
  .card--front{left:141px;background:var(--orange)}
  .card--back{left:466px;background:var(--blue)}

  .brand-mark{position:absolute;display:flex;align-items:center;gap:10px;font-family:"Mulish",sans-serif;font-weight:800;white-space:nowrap}
  .brand-mark__dot{display:block;border-radius:50%;background:var(--blue);flex:none}

  .card--front .brand-mark{left:0;right:0;top:80px;flex-direction:column;gap:18px;color:var(--white);font-size:31px}
  .card--front .brand-mark__dot{width:140px;height:140px}

  .tagline{position:absolute;left:0;right:0;top:300px;text-align:center;font-family:"Questrial",sans-serif;font-size:19px;line-height:31px;letter-spacing:.3px}

  .name-plate{position:absolute;left:18px;top:59px;width:274px;height:117px;background:var(--orange);border-radius:58px;border:3px solid var(--orange);box-shadow:inset 0 0 0 2px var(--white);text-align:center;padding-top:36px}
  .name-plate__name{font-weight:700;font-size:20px}
  .name-plate__role{font-family:"Mulish",sans-serif;font-style:italic;font-weight:400;font-size:15px;margin-top:2px}

  .contact-list{position:absolute;left:22px;top:232px;list-style:none}
  .contact-list__item{display:flex;align-items:center;height:42.5px}
  .contact-list__tag{width:62px;height:24px;border:1.5px solid var(--white);border-radius:12px;display:flex;align-items:center;justify-content:center;font-weight:700;font-size:14px;margin-right:19px}
  .contact-list__value{font-weight:700;font-size:15px}

  .comp-slip{position:absolute;left:30px;top:568px;width:373px;height:222px;background:var(--paper);border:1px solid var(--orange);box-shadow:5px 7px 9px var(--shadow);overflow:hidden}
  .comp-slip__band{position:absolute;left:0;top:0;width:373px;height:60px}
  .comp-slip__details{position:absolute;left:10px;top:6px;font-weight:700;font-size:8px;line-height:13px}
  .comp-slip .brand-mark{right:10px;top:46px;color:var(--blue);font-size:12px;gap:5px}
  .comp-slip .brand-mark__dot{width:22px;height:22px}
  .comp-slip__label{position:absolute;left:7px;top:159px;width:138px;height:51px;border-radius:26px;background:var(--orange);box-shadow:inset 0 0 0 2px var(--orange),inset 0 0 0 3.5px var(--white);text-align:center;font-weight:700;font-size:10px;line-height:13px;padding-top:12px}

  .letterhead{position:absolute;left:427px;top:569px;width:439px;height:581px;background:var(--paper);border:1px solid var(--orange);box-shadow:6px 8px 10px var(--shadow);overflow:hidden}
  .letterhead .brand-mark{right:16px;top:64px;color:var(--blue);font-size:14px;gap:6px}
  .letterhead .brand-mark__dot{width:26px;height:26px}
  .letterhead__footer-band{position:absolute;left:0;bottom:0;width:439px;height:72px}
  .letterhead__footer-text{position:absolute;left:0;right:0;bottom:8px;text-align:center;font-weight:700;font-size:7.5px;line-height:13px}

  .brand-mark--standalone{left:90px;top:960px;color:var(--blue);font-size:26px;gap:12px}
  .brand-mark--standalone .brand-mark__dot{width:56px;height:56px}
</style>
</head>
<body>

<section class="card card--front" aria-label="Business card front">
  <div class="brand-mark"><span class="brand-mark__dot"></span>TallCedarRun</div>
  <p class="tagline">Simple,<br>tailored,<br>effective<br>communication</p>
</section>

<section class="card card--back" aria-label="Business card back">
  <div class="name-plate">
    <p class="name-plate__name">Mr Owen Hartley</p>
    <p class="name-plate__role">Graphic Designer</p>
  </div>
  <ul class="contact-list">
    <li class="contact-list__item"><span class="contact-list__tag">T</span><span class="contact-list__value">020 55501234</span></li>
    <li class="contact-list__item"><span class="contact-list__tag">M</span><span class="contact-list__value">07 98765432</span></li>
    <li class="contact-list__item"><span class="contact-list__tag">E</span><span class="contact-list__value">hello@tallcedarrun.com</span></li>
    <li class="contact-list__item"><span class="contact-list__tag">W</span><span class="contact-list__value">www.tallcedarrun.com</span></li>
  </ul>
</section>

<section class="comp-slip" aria-label="Compliment slip">
  <svg class="comp-slip__band" viewBox="0 0 373 60" aria-hidden="true">
    <path d="M0 0 H373 V40 Q190 30 0 50 Z" fill="var(--orange)"/>
  </svg>
  <p class="comp-slip__details">18 Willow Lane, P.O.Box 4821, London, UK &bull; T&nbsp; 020 55501234<br>F&nbsp; 020 55501235 &bull; www.tallcedarrun.com &bull; info@tallcedarrun.com</p>
  <div class="brand-mark"><span class="brand-mark__dot"></span>TallCedarRun</div>
  <div class="comp-slip__label">With<br>Compliments</div>
</section>

<section class="letterhead" aria-label="Letterhead">
  <div class="brand-mark"><span class="brand-mark__dot"></span>TallCedarRun</div>
  <svg class="letterhead__footer-band" viewBox="0 0 439 72" aria-hidden="true">
    <path d="M0 72 V38 Q219 -8 439 38 V72 Z" fill="var(--orange)"/>
  </svg>
  <p class="letterhead__footer-text">18 Willow Lane, P.O.Box 4821, London, UK<br>T&nbsp; 020 55501234 &nbsp;&bull;&nbsp; F&nbsp; 020 55501235 &nbsp;&bull;&nbsp; www.tallcedarrun.com &nbsp;&bull;&nbsp; info@tallcedarrun.com</p>
</section>

<div class="brand-mark brand-mark--standalone"><span class="brand-mark__dot"></span>TallCedarRun</div>

</body>
</html>
```